Navigate the Underground Car Park to 7K3R Vet Clinic

Eye-catching signage for Underground Carpark.
We want to help new Clients, or those with bad senses of direction, to the correct Lift Lobby.
We want to be able to say 'Just follow the signs'.

It can be confusing and many other business have utilised some of the pillars in the carpark to guide their customers to the right place.

People don't want to walk far with sick animals so it is important they get to the right Lift Lobby.
Updates

We are thinking instead of 'Just Follow the Signs,We would like to try:'Looking for us?' (Large Text)'Follow the Signs (much smaller Text)Also, it is very useful to see the proposed sign dropped on to the photo of the car park pillars I included.Many thanks Added Friday, June 16, 2017

Target Market(s)

Customers, coming for the 1st time, trying to navigate the Underground CarPark towards the appropriate Lift lobby

Industry/Entity Type

Veterinary

Font styles to use
Serif

Colors
f78f20
00a990
0455a3

Requirements
Must have
• Logo.
• Bright. Clear. Not too cluttered.
• Warmth. Humour. Approachable.
• Please include: Building 4, Mezzanine Level
Nice to have
• Please look at our FB pages and Instagram page @7k3rvetclinic for a good feel of who we are.
• Some level of style or image continuity with the Pet Tips Poster (see attached file)
Should not have
• Not have a medical feel

```html
<!DOCTYPE html>
<html lang="en">
<head>
<meta charset="utf-8">
<title>7K3R Vet Clinic – Car Park Wayfinding Signs</title>
<link rel="stylesheet" href="https://fonts.googleapis.com/css2?family=Chewy&family=Didact+Gothic&display=swap">
<style>
  :root {
    --orange: #f78f20;
    --teal: #00a990;
    --blue: #0455a3;
    --ink: #1f1f2a;
    --paper: #ffffff;
    --backdrop: #e4e4e4;
  }
  * { box-sizing: border-box; margin: 0; padding: 0; }
  html, body { width: 1200px; height: 1200px; overflow: hidden; }
  body {
    background: var(--backdrop);
    position: relative;
    font-family: "Didact Gothic", sans-serif;
  }
  .sign {
    position: absolute;
    top: 230px;
    width: 520px;
    height: 740px;
    background: var(--paper);
    border: 8px solid var(--blue);
    box-shadow: 6px 8px 14px rgba(0,0,0,0.28);
  }
  .sign--lead { left: 60px; }
  .sign--way { left: 620px; }

  .paw { position: absolute; width: 74px; height: 70px; }
  .paw--top-left { left: 14px; top: 16px; }
  .paw--right { right: 26px; top: 88px; }

  .brand {
    position: absolute;
    top: 92px;
    left: 0; right: 0;
    display: flex;
    justify-content: center;
    align-items: center;
    gap: 10px;
  }
  .brand__dot {
    width: 22px; height: 22px;
    border-radius: 50%;
    background: var(--teal);
  }
  .brand__name {
    font-family: "Didact Gothic", sans-serif;
    font-size: 26px;
    color: var(--orange);
    letter-spacing: 0.5px;
  }

  .headline {
    position: absolute;
    top: 150px;
    left: 20px; right: 20px;
    text-align: center;
    font-family: "Chewy", cursive;
    font-size: 80px;
    line-height: 0.86;
    color: var(--orange);
    -webkit-text-stroke: 4px var(--blue);
    paint-order: stroke fill;
    transform: rotate(-2deg);
  }

  .direction-arrow {
    position: absolute;
    left: 32px;
    top: 320px;
    width: 100px;
    height: 306px;
  }

  .mascot {
    position: absolute;
    left: 160px;
    top: 330px;
    width: 320px;
    height: 310px;
    border-radius: 40% 40% 30% 30%;
    background: radial-gradient(ellipse at 50% 40%, #c9743a 0%, #e9c9a8 45%, #f2ece6 75%, #ffffff 100%);
  }

  .location {
    position: absolute;
    bottom: 18px;
    left: 0; right: 0;
    text-align: center;
    font-size: 29px;
    color: var(--ink);
  }
</style>
</head>
<body>

<svg width="0" height="0" style="position:absolute">
  <defs>
    <symbol id="paw-icon" viewBox="0 0 74 70">
      <ellipse cx="14" cy="30" rx="9" ry="12" transform="rotate(-25 14 30)"/>
      <ellipse cx="29" cy="14" rx="9" ry="12" transform="rotate(-8 29 14)"/>
      <ellipse cx="47" cy="14" rx="9" ry="12" transform="rotate(10 47 14)"/>
      <ellipse cx="61" cy="31" rx="9" ry="12" transform="rotate(28 61 31)"/>
      <path d="M37 34 C24 34 16 48 18 57 C20 66 30 62 37 62 C44 62 54 66 56 57 C58 48 50 34 37 34 Z"/>
    </symbol>
    <symbol id="arrow-up" viewBox="0 0 100 306">
      <polygon points="50,0 100,96 68,96 68,176 32,176 32,96 0,96"/>
      <rect x="20" y="182" width="60" height="28"/>
      <rect x="20" y="224" width="60" height="18"/>
      <rect x="20" y="260" width="60" height="12"/>
      <rect x="20" y="296" width="60" height="9"/>
    </symbol>
  </defs>
</svg>

<section class="sign sign--lead">
  <svg class="paw paw--top-left" fill="var(--teal)"><use href="#paw-icon"/></svg>
  <svg class="paw paw--right" fill="var(--teal)"><use href="#paw-icon"/></svg>
  <div class="brand">
    <span class="brand__dot"></span>
    <span class="brand__name">7K3R Vet Clinic</span>
  </div>
  <h1 class="headline">Follow my<br>lead, human!</h1>
  <svg class="direction-arrow" fill="var(--teal)"><use href="#arrow-up"/></svg>
  <div class="mascot" role="img" aria-label="Cartoon beagle standing happily with tongue out, tail wagging"></div>
  <p class="location">Building 4, Mezzanine Level</p>
</section>

<section class="sign sign--way">
  <svg class="paw paw--top-left" fill="var(--teal)"><use href="#paw-icon"/></svg>
  <svg class="paw paw--right" fill="var(--teal)"><use href="#paw-icon"/></svg>
  <div class="brand">
    <span class="brand__dot"></span>
    <span class="brand__name">7K3R Vet Clinic</span>
  </div>
  <h1 class="headline">Yup, right<br>this way!</h1>
  <svg class="direction-arrow" fill="var(--teal)"><use href="#arrow-up"/></svg>
  <div class="mascot" role="img" aria-label="Cartoon beagle bounding forward with ears flapping and tongue out"></div>
  <p class="location">Building 4, Mezzanine Level</p>
</section>

</body>
</html>
```